Business Card Design

I am nail technician working from home in Fernwick Rise, Perth and I require new business cards. I only work with Gel medium for nail extensions using tips or I can also do sculpture nails. I specialise in hand painted nail art using water based acrylic paint and nail polish. As the name suggest I love all things "Shimmer" so I would love something that reflects this while also being professional. I'm also on Chatterly and would the Chatterly logo.

Contact Information for Business Card

Shimmer Bay nail designs,Rosanne ,0417859263, ShimmerBaynaildesigns@quellmail.com, nail technician specialising in hand painted nail art, only using a Gel medium

```html
<!DOCTYPE html>
<html lang="en">
<head>
<meta charset="utf-8">
<title>Rosanne – Shimmer Bay nail designs</title>
<link rel="stylesheet" href="https://fonts.googleapis.com/css2?family=Pinyon+Script&family=Questrial&display=swap">
<style>
  :root {
    --glitter-deep: #8e1230;
    --glitter-mid: #c42a4e;
    --glitter-light: #e2547a;
    --gold-light: #fff3a6;
    --gold-mid: #e8b52c;
    --gold-dark: #9a6a0c;
    --ink-white: #ffffff;
    --badge: #3b5a9a;
  }
  html, body {
    margin: 0;
    padding: 0;
    width: 1200px;
    height: 741px;
    overflow: hidden;
    background: #ffffff;
  }
  .card {
    position: relative;
    width: 1200px;
    height: 741px;
    overflow: hidden;
    font-family: "Questrial", "Helvetica Neue", Arial, sans-serif;
    color: var(--ink-white);
  }
  .card__backdrop {
    position: absolute;
    inset: 0;
    background:
      radial-gradient(ellipse at 50% 40%, var(--glitter-light) 0%, transparent 60%),
      radial-gradient(ellipse at 80% 85%, var(--glitter-mid) 0%, transparent 55%),
      linear-gradient(160deg, var(--glitter-mid) 0%, var(--glitter-deep) 100%);
  }
  .card__name {
    position: absolute;
    left: 0;
    right: 0;
    top: 118px;
    margin: 0;
    text-align: center;
    font-family: "Pinyon Script", "Times New Roman", serif;
    font-weight: 400;
    font-size: 158px;
    line-height: 1.1;
    background: linear-gradient(180deg, var(--gold-light) 0%, var(--gold-mid) 45%, var(--gold-dark) 100%);
    -webkit-background-clip: text;
    background-clip: text;
    color: transparent;
  }
  .card__tagline {
    position: absolute;
    left: 0;
    right: 0;
    top: 328px;
    margin: 0;
    text-align: center;
    font-size: 30px;
    line-height: 39px;
  }
  .card__contact {
    position: absolute;
    left: 0;
    right: 0;
    top: 452px;
    margin: 0;
    text-align: center;
    font-size: 43px;
    line-height: 1;
  }
  .contact__phone { display: block; height: 70px; }
  .contact__social {
    display: flex;
    justify-content: center;
    align-items: center;
    gap: 14px;
    height: 68px;
  }
  .social__badge {
    width: 36px;
    height: 36px;
    background: var(--badge);
  }
  .contact__email { display: block; margin-top: 8px; }
</style>
</head>
<body>
  <main class="card">
    <div class="card__backdrop" role="img" aria-label="Sparkling red glitter background"></div>
    <h1 class="card__name">Rosanne</h1>
    <p class="card__tagline">Nail technician specialising in hand painted nail art,<br>only using a Gel medium</p>
    <address class="card__contact" style="font-style: normal;">
      <span class="contact__phone">0417859263</span>
      <span class="contact__social">
        <span class="social__badge" aria-hidden="true"></span>
        <span class="social__network">Chatterly</span>
        <span class="social__handle">/ShimmerBaynaildesign</span>
      </span>
      <span class="contact__email">ShimmerBaynaildesigns@quellmail.com</span>
    </address>
  </main>
</body>
</html>
```